Creating the look & feel for a Commercial Mortgage company in Canada

We need graphics for a corporate brochure, updated website and large signage located on development properties. We are open to a logo refresh - NOT a redesign. We are a commercial real estate mortgage broker located in Toronto, Canada. Let me try and simplify what we do. We find the money for customers (builders and developers)so that they build very large housing/townhouse/condo properties. We also have funds to invest.. this is important because if builders perceived we have money this will further their interest in our business. Our base color is green - we need a CKMY or PMS color defined. We may need to add a color or two to add some depth. We are trustworthy, honest, a little hip or cool,, innovative and very detail orientated. We want to communicate that have money funds or access to funds AND the customer comes first. We put a great deal of effort into underwriting deals to ensure customer success. CURRENT website : https://velmacrest.com/
Updates

I have updated my brief to make it clearer, please have a look thank you

Target Market(s)

two target markets:
Developer: Male, 40-50 yrs++, developing wealth, like to enjoy his money with his family (ie vacations, high-end cars)
investor: Male 60 yrs ++, wealthy, continuously reinvesting money, has a least 1 expensive specialty hobby ie art collection, wine tasting & collecting/buying

Font styles to use
Serif
Sans Serif

Colors
9bcb3c

Requirements
Must have
• GRAPHICS - that can be used across several mediums
• GRAPHICS for a Large Sign - design sign for construction site
• color suggestions with pms #'s
• Logo - refresh logo OR creating an icon for Velma crest
• GRAPHICS for a Brochure - example brochure might be 2 page - 8X11, back-to-back, graphics; specifically header, footer, icons, pictures/visuals
• GRAPHICS for a Website - visuals, pictures, icons, header, footer
Nice to have
• additional ideas for the website

```html
<!DOCTYPE html>
<html lang="en">
<head>
<meta charset="utf-8">
<title>Velma Crest – Header, Band and Footer Graphics</title>
<link rel="stylesheet" href="https://fonts.googleapis.com/css2?family=Lato:ital,wght@0,400;0,700;1,400;1,700&family=Orbitron:wght@700&display=swap">
<style>
  :root {
    --green-deep: #0b2a10;
    --green-dark: #163f1c;
    --green-mid: #2f6a35;
    --green-soft: #5a8a5c;
    --green-brand: #5fa03f;
    --green-bright: #9bcb3c;
    --white: #ffffff;
    --ink: #1c1c1c;
    --muted: #3d5a40;
  }
  * { margin: 0; padding: 0; box-sizing: border-box; }
  html, body { width: 1200px; height: 800px; overflow: hidden; background: var(--white); }
  body { position: relative; font-family: "Lato", sans-serif; }

  .panel { position: absolute; left: 0; width: 1200px; height: 200px; overflow: hidden; }
  .panel svg.art { position: absolute; inset: 0; }
  .web-header { top: 0; }
  .print-band { top: 300px; background: var(--white); }
  .site-footer { top: 600px; }

  .brand { position: absolute; display: flex; align-items: center; gap: 14px; }
  .brand-mark { width: 46px; height: 46px; background: var(--green-brand); }
  .brand-name {
    font-family: "Lato", sans-serif; font-weight: 700; font-size: 40px;
    letter-spacing: 2px; line-height: 1; color: var(--green-bright);
  }
  .brand-on-light .brand-name { color: var(--green-brand); }

  .tagline {
    position: absolute; left: 32px; top: 150px;
    font-family: "Orbitron", sans-serif; font-weight: 700; font-size: 19px;
    letter-spacing: 3px; color: var(--white);
  }
  .header-url {
    position: absolute; left: 33px; top: 173px;
    font-style: italic; font-size: 16px; color: var(--muted);
  }
  .utility {
    position: absolute; top: 11px; right: 24px; display: flex; gap: 38px;
    font-style: italic; font-size: 14px; color: var(--white); align-items: center;
  }
  .utility span { display: flex; align-items: center; gap: 7px; }
  .main-nav {
    position: absolute; top: 171px; left: 503px; display: flex; gap: 0;
    font-size: 14px; color: var(--white);
  }
  .main-nav a { color: inherit; text-decoration: none; margin-right: 24px; }
  .main-nav a.current { color: var(--green-bright); }
  .main-nav a:last-child { margin-right: 0; margin-left: -4px; }

  .contact-row {
    position: absolute; top: 62px; left: 98px; display: flex; gap: 28px;
    font-style: italic; font-weight: 700; font-size: 17px; color: var(--ink);
  }
  .contact-row span { display: flex; align-items: center; gap: 9px; }
  .band-url {
    position: absolute; top: 175px; left: 893px;
    font-size: 15px; letter-spacing: 1.5px; color: var(--white);
  }

  .footer-contacts {
    position: absolute; top: 42px; right: 84px; display: flex; flex-direction: column;
    align-items: flex-end; gap: 14px; font-size: 14px; letter-spacing: 1.6px; color: var(--white);
  }
  .footer-contacts span { display: flex; align-items: center; gap: 16px; }
  .footer-contacts svg { width: 22px; height: 22px; }
  .footer-url {
    position: absolute; top: 174px; left: 98px;
    font-size: 14px; letter-spacing: 1.5px; color: var(--green-brand);
  }
</style>
</head>
<body>

<!-- Website header -->
<header class="panel web-header">
  <svg class="art" width="1200" height="200" viewBox="0 0 1200 200">
    <defs>
      <linearGradient id="hdrBg" x1="0" y1="0" x2="0" y2="1">
        <stop offset="0" stop-color="#1f4a22"/><stop offset="1" stop-color="#0a2410"/>
      </linearGradient>
      <linearGradient id="hdrScene" x1="0" y1="0" x2="1" y2="0">
        <stop offset="0" stop-color="#0f2a12"/><stop offset="0.6" stop-color="#2d6a2e"/><stop offset="1" stop-color="#4f9a45"/>
      </linearGradient>
    </defs>
    <rect width="1200" height="200" fill="url(#hdrBg)"/>
    <path d="M400,200 C440,120 620,50 1200,0 L1200,200 Z" fill="url(#hdrScene)" role="img" aria-label="Digital data city backdrop in green tones"/>
    <path d="M490,155 L1200,152 L1200,200 L478,200 Z" fill="#0b2a10" opacity="0.55"/>
    <path d="M490,155 L1200,152" stroke="#5a8a5c" stroke-width="3" fill="none"/>
  </svg>
  <div class="brand" style="left:34px; top:52px;"><div class="brand-mark"></div><div class="brand-name">VELMA CREST</div></div>
  <div class="tagline">YOUR FINANCIAL SOLUTION</div>
  <div class="header-url">https://velmacrest.com</div>
  <div class="utility">
    <span><svg width="16" height="16" viewBox="0 0 16 16"><circle cx="8" cy="8" r="7" fill="none" stroke="#fff" stroke-width="1.4"/><path d="M5.5,4.5 l1.5,0 l0.6,2 l-1,0.8 c0.5,1 1.2,1.7 2.1,2.1 l0.8,-1 l2,0.6 l0,1.5 c-3,0.5 -6.5,-3 -6,-6z" fill="#fff"/></svg>416-555-0192</span>
    <span>Login</span>
  </div>
  <nav class="main-nav">
    <a class="current" href="#">Home</a><a href="#">About Us</a><a href="#">Contact Us</a><a href="#">Services</a><a href="#">Advisory Services</a><a href="#">Transactions Portfolio</a><a href="#">Lot Value Report</a>
  </nav>
</header>

<!-- Print band -->
<section class="panel print-band">
  <svg class="art" width="1200" height="200" viewBox="0 0 1200 200">
    <defs>
      <linearGradient id="swoop" x1="0" y1="0" x2="1" y2="0">
        <stop offset="0" stop-color="#2f6a35"/><stop offset="1" stop-color="#0b2a10"/>
      </linearGradient>
      <linearGradient id="bandBase" x1="0" y1="0" x2="0" y2="1">
        <stop offset="0" stop-color="#2f6a35"/><stop offset="1" stop-color="#0b2a10"/>
      </linearGradient>
    </defs>
    <path d="M0,0 L642,0 C420,4 120,18 0,110 Z" fill="url(#swoop)"/>
    <path d="M0,0 L642,0 C400,6 120,30 20,80 C70,40 250,8 642,0" fill="#5a8a5c" opacity="0.5"/>
    <path d="M0,200 C150,150 340,113 540,115 C780,118 980,165 1100,145 C1160,135 1190,115 1200,100 L1200,200 Z" fill="url(#bandBase)"/>
    <path d="M0,200 C150,150 340,113 540,115 C780,118 980,165 1100,145 C1000,148 780,128 540,125 C350,125 170,160 60,200 Z" fill="#5a8a5c"/>
    <path d="M440,135 C520,140 570,170 590,200 L550,200 C530,175 490,150 440,135 Z" fill="#5a8a5c"/>
  </svg>
  <div class="contact-row">
    <span><svg width="18" height="22" viewBox="0 0 18 22"><path d="M3,1 l4,0 l1.5,5 l-2.5,2 c1.2,2.6 3,4.6 5.5,6 l2,-2.5 l4.5,1.5 l0,4.5 c-8,1.5 -16,-8 -15,-16.5z" fill="#5fa03f"/></svg>416-555-0192</span>
    <span><svg width="24" height="22" viewBox="0 0 24 22"><path d="M12,1 L23,11 L20,11 L20,21 L14,21 L14,14 L10,14 L10,21 L4,21 L4,11 L1,11 Z" fill="#5fa03f"/></svg>https://velmacrest.com</span>
    <span style="margin-left:6px;"><svg width="24" height="18" viewBox="0 0 24 18"><rect x="1" y="1" width="22" height="16" fill="none" stroke="#5fa03f" stroke-width="2"/><path d="M1,1 L12,10 L23,1 M1,17 L9,8 M23,17 L15,8" stroke="#5fa03f" stroke-width="2" fill="none"/></svg>email@velmacrest.com</span>
  </div>
  <div class="brand brand-on-light" style="left:870px; top:54px;"><div class="brand-mark"></div><div class="brand-name">VELMA CREST</div></div>
  <div class="band-url">https://velmacrest.com</div>
</section>

<!-- Website footer -->
<footer class="panel site-footer">
  <svg class="art" width="1200" height="200" viewBox="0 0 1200 200">
    <defs>
      <linearGradient id="ftBg" x1="0" y1="0" x2="0" y2="1">
        <stop offset="0" stop-color="#2a5e2e"/><stop offset="1" stop-color="#0b2a10"/>
      </linearGradient>
      <linearGradient id="ftScene" x1="0" y1="0" x2="1" y2="0">
        <stop offset="0" stop-color="#143717"/><stop offset="0.7" stop-color="#2d6a2e"/><stop offset="1" stop-color="#3f8a3c"/>
      </linearGradient>
    </defs>
    <rect width="1200" height="200" fill="url(#ftBg)"/>
    <path d="M300,60 C600,20 900,10 1200,0 L1200,160 C900,150 600,150 300,160 Z" fill="url(#ftScene)" role="img" aria-label="Digital data city backdrop in green tones"/>
    <path d="M0,160 C300,140 700,130 1000,145 C1100,150 1160,165 1200,180 L1200,200 L0,200 Z" fill="#0b2a10"/>
    <path d="M0,160 C300,140 700,130 1000,145 C700,142 300,150 0,175 Z" fill="#5a8a5c"/>
    <path d="M620,200 C680,160 800,145 900,150 C820,160 720,175 680,200 Z" fill="#5a8a5c"/>
  </svg>
  <div class="brand" style="left:76px; top:76px;"><div class="brand-mark"></div><div class="brand-name">VELMA CREST</div></div>
  <div class="footer-contacts">
    <span>416-555-0192<svg viewBox="0 0 22 22"><path d="M5,1 l4,0 l1.5,5 l-2.5,2 c1.2,2.6 3,4.6 5.5,6 l2,-2.5 l4.5,1.5 l0,4.5 c-8,1.5 -16,-8 -15,-16.5z" fill="#fff"/></svg></span>
    <span>email@velmacrest.com<svg viewBox="0 0 22 22"><rect x="2" y="5" width="18" height="12" fill="none" stroke="#fff" stroke-width="1.6"/><path d="M2,5 L11,12 L20,5 M2,17 L9,10 M20,17 L13,10" stroke="#fff" stroke-width="1.6" fill="none"/></svg></span>
    <span>https://velmacrest.com<svg viewBox="0 0 22 22"><path d="M11,1 L21,10 L18,10 L18,21 L13,21 L13,15 L9,15 L9,21 L4,21 L4,10 L1,10 Z" fill="#fff"/></svg></span>
  </div>
  <div class="footer-url">https://velmacrest.com</div>
</footer>

</body>
</html>
```